PTA Business Card

Seeking design for a business card, standard size. It is going to be for myself in regards to PTA - details:

Hollis Brantley Elementary School
PTA President
Peter Lund
563-555-0147
Lundy1984@mailbarn.example

Requirement:
Facebook icon? "Hollis Brantley PTA Rusk"
Twitter thing? I am new to twitter so not sure what to put, here is the link:
https://twitter.example/HBRoversPTA

I was thinking on the front would be a notebook paper background? Not a requirement but was thinking it would look cool?

Total freedom here, let your creativity spread because I don't have any suggestions for design, sorry. Colors of school district are black and yellow.

Backside I am not sure exactly what to put on it.

```html
<!DOCTYPE html>
<html lang="en">
<head>
<meta charset="utf-8">
<title>Peter Lund – PTA President</title>
<link rel="stylesheet" href="https://fonts.googleapis.com/css2?family=Roboto+Condensed:wght@300;700&family=Roboto:wght@400;700&display=swap">
<style>
  :root {
    --card-yellow: #eaff00;
    --ink: #111111;
    --shard-dark: rgba(17, 17, 17, 0.55);
    --shard-soft: rgba(17, 17, 17, 0.08);
  }
  html, body {
    margin: 0;
    padding: 0;
    width: 1200px;
    height: 632px;
    overflow: hidden;
    background: var(--card-yellow);
  }
  .card {
    position: relative;
    width: 1200px;
    height: 632px;
    background: var(--card-yellow);
    color: var(--ink);
    font-family: "Roboto Condensed", "Arial Narrow", sans-serif;
    overflow: hidden;
  }
  .line {
    position: absolute;
    left: 159px;
    margin: 0;
    white-space: nowrap;
  }
  .bold { font-weight: 700; }
  .light { font-weight: 300; }
  .size-lg { font-size: 55px; line-height: 55px; }
  .size-md { font-size: 50px; line-height: 50px; }
  .name-first { top: 72px; }
  .name-last  { top: 117px; }
  .role {
    top: 169px;
    font-family: "Roboto", Arial, sans-serif;
    font-size: 18px;
    line-height: 18px;
    letter-spacing: 2px;
    font-weight: 400;
  }
  .role strong { font-weight: 700; }
  .phone-area { top: 208px; }
  .phone-local { top: 252px; }
  .email-user { top: 317px; }
  .email-domain { top: 366px; }
  .icon {
    position: absolute;
    fill: none;
    stroke: var(--ink);
    stroke-width: 4;
    stroke-linejoin: round;
    stroke-linecap: round;
  }
  .icon-person { left: 100px; top: 84px; width: 58px; height: 68px; }
  .icon-phone  { left: 96px;  top: 222px; width: 62px; height: 62px; }
  .icon-mail   { left: 95px;  top: 348px; width: 60px; height: 42px; }
  .shards {
    position: absolute;
  }
  .shards-top {
    right: 0;
    top: 0;
    width: 440px;
    height: 240px;
    background: radial-gradient(ellipse at 75% 35%, var(--shard-dark) 0%, var(--shard-soft) 45%, transparent 72%);
  }
  .shards-bottom {
    right: 0;
    bottom: 0;
    width: 200px;
    height: 150px;
    background: radial-gradient(ellipse at 85% 70%, var(--shard-dark) 0%, var(--shard-soft) 45%, transparent 75%);
  }
  .shards-mid {
    right: 140px;
    top: 318px;
    width: 110px;
    height: 40px;
    background: radial-gradient(ellipse at center, var(--shard-dark) 0%, transparent 70%);
  }
</style>
</head>
<body>
<main class="card">
  <div class="shards shards-top" role="img" aria-label="Scattered dark glass shards decoration"></div>
  <div class="shards shards-mid" role="img" aria-label="Single dark glass shard"></div>
  <div class="shards shards-bottom" role="img" aria-label="Scattered dark glass shards decoration"></div>

  <svg class="icon icon-person" viewBox="0 0 58 68" aria-hidden="true">
    <circle cx="29" cy="16" r="12"/>
    <path d="M4 52 C4 38 16 32 29 32 C42 32 54 38 54 52 C54 60 42 64 29 64 C16 64 4 60 4 52 Z"/>
    <path d="M18 36 L29 50 L40 36"/>
    <path d="M29 50 L29 60"/>
  </svg>

  <p class="line size-lg bold name-first">PETER</p>
  <p class="line size-lg light name-last">LUND</p>
  <p class="line role"><strong>PTA</strong> PRESIDENT</p>

  <svg class="icon icon-phone" viewBox="0 0 62 62" aria-hidden="true">
    <path d="M6 16 L16 6 L26 18 L20 24 C23 31 31 39 38 42 L44 36 L56 46 L46 56 C28 54 8 34 6 16 Z"/>
    <path d="M12 12 L20 22"/>
    <path d="M40 50 L50 42"/>
  </svg>

  <p class="line size-md light phone-area">563</p>
  <p class="line size-md light phone-local">555-0147</p>

  <svg class="icon icon-mail" viewBox="0 0 60 42" aria-hidden="true">
    <rect x="3" y="3" width="54" height="36" rx="2"/>
    <path d="M3 3 L30 24 L57 3"/>
    <path d="M3 39 L23 19"/>
    <path d="M57 39 L37 19"/>
  </svg>

  <p class="line size-lg bold email-user">Lundy1984</p>
  <p class="line size-md light email-domain">@mailbarn.example</p>
</main>
</body>
</html>
```